Web Site for Strategy and Technology Consulting Company

We are looking for a website design that engages potential customers to understand our services and contact us. In this contest, we are looking for a homepage design, but the winning designer will be favored for the design of some of the more complicated interior pages of the site. An additional contest (or contests) for these pages will be added soon.

PLATROM AND RESPONSIVE DESIGN
The site will be implemented in WordPress using the Elementor page builder.
We are looking for a design that will look good on phones are well as laptop browsers.

UPLOADED FILES INCLUDE:
1a A wireframe of the homepage we are looking for. The Uploaded PDF also includes a draft of the text proposed for the homepage. Designers are free to go beyond the wireframe, but all elements of the wireframe should be included.
1b A Word document with the draft text of the homepage.
2a-d The Norvalith logo. Two versions are included – a dark version which works well against a light background, and a light version which works well against a dark background.
3 The Norvalith color palette with HEX and RGB values. Designers are not limited to this palette, but colors should be complementary.
4 A draft of the homepage menu
5 Service sheets with information on the services we provide

MORE ABOUT NORVALITH
Norvalith is a consulting company focused on transforming businesses through software. Our tagline, “Transformation Delivered,” recognizes the gap business often have between business transformation and the software they end up with. By listening to our customers and understanding their vision and where they are, we help get our customers where they want to go.

We increase our capability by working with many consultants and partners, allowing us to provide our customers with the best people and the software that best suits them.

Industry/Entity Type

Consulting

Number of Pages Required

1 page

Font styles to use
Sans Serif

Requirements
Must have
• the content represented on the wireframe uploaded
Nice to have
• interactive features, such as roll-over icons that reveal additional information

```html
<!DOCTYPE html>
<html lang="en">
<head>
<meta charset="utf-8">
<title>Norvalith — Transformation Delivered</title>
<link rel="stylesheet" href="https://fonts.googleapis.com/css2?family=Russo+One&family=Roboto:wght@300;400;500;700&display=swap">
<style>
:root{
  --navy:#1d3f7a;
  --navy-dark:#14295a;
  --blue:#2f6fc4;
  --yellow:#f3c316;
  --ink:#3a3f4a;
  --muted:#7a808c;
  --line:#dfe3ea;
  --light:#f1f2f5;
  --soft-blue:#cfe0f3;
  --white:#ffffff;
  --hero-a:#4b2a8c;
  --hero-b:#c48ad8;
  --hero-c:#f0c6e6;
  --foot-bar:#9aa6b4;
  --head:"Russo One",sans-serif;
  --body:"Roboto",sans-serif;
}
*{box-sizing:border-box;margin:0;padding:0}
html,body{width:1200px;height:3724px;overflow:hidden;background:var(--white);font-family:var(--body);color:var(--ink)}
section,header,footer{position:relative;width:1200px;overflow:hidden}
.btn{display:inline-flex;align-items:center;gap:10px;background:var(--navy);color:#fff;border-radius:24px;padding:12px 24px;font:700 13px var(--body);letter-spacing:.5px;text-transform:uppercase}
.btn .ico{width:18px;height:18px;border-radius:50%;background:#fff;display:inline-block;position:relative}
.btn .ico::after{content:"";position:absolute;left:6px;top:5px;border-left:6px solid var(--navy);border-top:4px solid transparent;border-bottom:4px solid transparent}

/* header */
.site-header{height:64px;display:flex;align-items:center;justify-content:space-between;padding:0 150px 0 160px;border-top:4px solid var(--yellow)}
.brand{display:flex;align-items:center;gap:10px;font:400 34px var(--head);color:var(--navy)}
.brand .dot{width:14px;height:14px;border-radius:50%;background:var(--navy)}
.main-nav{display:flex;gap:22px;font:500 12px var(--body);color:var(--navy);text-transform:uppercase}
.main-nav .active{color:var(--yellow)}

/* hero */
.hero{height:536px;background:linear-gradient(180deg,var(--hero-a) 0%,#8b5cc2 35%,var(--hero-b) 70%,var(--hero-c) 100%)}
.hero-photo{position:absolute;inset:0;background:linear-gradient(180deg,rgba(255,255,255,0) 45%,rgba(60,40,110,.35) 75%,rgba(255,255,255,.1) 100%)}
.hero-title{position:absolute;top:200px;width:100%;text-align:center;font:400 58px/1.05 var(--head);color:#fff;letter-spacing:2px;text-transform:uppercase;text-shadow:0 0 14px rgba(255,255,255,.6)}
.hero-wave{position:absolute;bottom:-1px;left:0}

/* intro */
.intro{height:480px}
.intro-media{position:absolute;left:110px;top:10px;width:430px;height:420px}
.intro-copy{position:absolute;left:612px;top:60px;width:440px}
.section-title{font:400 26px/1.15 var(--head);color:var(--navy);text-transform:uppercase}
.intro-copy p{font-size:12px;line-height:1.6;color:var(--muted);margin-top:12px}
.ticks{list-style:none;margin-top:12px}
.ticks li{position:relative;padding-left:24px;font-size:12px;line-height:1.5;color:var(--ink);margin-bottom:8px}
.ticks li::before{content:"";position:absolute;left:0;top:3px;width:12px;height:12px;background:var(--navy)}
.ticks li:nth-child(even)::before{background:var(--yellow)}
.intro-copy .btn{margin-top:18px}
.badge{position:absolute;left:128px;top:340px;width:150px;background:var(--yellow);color:var(--navy-dark);font:700 10px/1.3 var(--body);text-transform:uppercase;padding:10px 12px;border-radius:4px}

/* services */
.services{height:460px;background:var(--light)}
.services .section-title{text-align:center;margin-top:70px;font-size:30px}
.services .sub{text-align:center;font-size:13px;color:var(--muted);margin-top:10px}
.service-row{position:absolute;top:240px;left:160px;display:flex;gap:30px}
.service-card{width:200px;height:150px;background:#fff;border-radius:18px;padding:70px 14px 0;text-align:center;position:relative}
.service-card:nth-child(1){border-left:4px solid var(--blue)}
.service-card:nth-child(2){border-left:4px solid var(--navy)}
.service-card:nth-child(3){border-left:4px solid var(--yellow)}
.service-card:nth-child(4){border-left:4px solid var(--blue)}
.service-icon{position:absolute;top:-30px;left:64px;width:72px;height:72px;border:3px solid var(--navy);border-radius:16px;background:#fff;display:flex;align-items:center;justify-content:center}
.service-card:nth-child(3) .service-icon{border-color:var(--yellow)}
.service-card h3{font:500 14px var(--body);color:var(--navy)}
.service-card p{font-size:10px;color:var(--muted);margin-top:6px;line-height:1.4}

/* people */
.people{height:520px}
.people-copy{position:absolute;left:160px;top:70px;width:400px}
.people-copy .section-title{font-size:28px;padding-bottom:8px;display:inline-block;border-bottom:3px solid var(--yellow)}
.people-copy p{font-size:12px;line-height:1.6;color:var(--muted);margin-top:12px}
.people-copy .btn{margin-top:22px}
.people-media{position:absolute;left:690px;top:40px;width:420px;height:420px}

/* testimonials */
.testimonials{height:380px;background:var(--light)}
.quote-card{position:absolute;top:60px;height:260px;border-radius:22px;padding:110px 40px 0;text-align:center;font-size:11px;line-height:1.6;color:var(--muted)}
.quote-card.side{width:330px;background:#e3e6ea;opacity:.55;padding-top:90px}
.quote-card.left{left:-120px}
.quote-card.right{left:990px}
.quote-card.center{left:250px;width:700px;background:var(--soft-blue);color:#4c5666}
.avatar{position:absolute;top:26px;left:315px;width:70px;height:70px;border-radius:50%;background:linear-gradient(135deg,#c9a88e,#6f5a52);border:3px solid #fff}
.quote-name{margin-top:14px;font:700 13px var(--body);color:var(--navy);letter-spacing:1px}
.arrow{position:absolute;top:172px;width:34px;height:34px;border-radius:50%;background:#2c3440;display:flex;align-items:center;justify-content:center}

/* technologies */
.technologies{height:480px}
.technologies .section-title{text-align:center;margin-top:40px;font-size:30px}
.tech-row{position:absolute;top:110px;left:160px;display:flex;gap:20px}
.tech-tile{position:relative;width:280px;height:340px;overflow:hidden}
.tech-tile .fill{position:absolute;inset:0}
.tech-tile .label{position:absolute;left:0;bottom:0;width:210px;background:var(--yellow);clip-path:polygon(0 0,80% 0,100% 100%,0 100%);padding:14px 16px;font:700 13px/1.2 var(--body);color:var(--navy-dark);text-transform:uppercase}

/* partners */
.partners{height:160px}
.partner-row{position:absolute;top:30px;left:180px;display:flex;gap:24px}
.partner{width:190px;height:90px;background:#fff;border:1px solid var(--line);border-radius:6px;display:flex;align-items:center;justify-content:center;box-shadow:0 3px 10px rgba(0,0,0,.06)}
.partner .mark{height:26px;border-radius:13px}

/* footer */
.site-footer{height:580px;background:var(--light)}
.footer-wave{position:absolute;top:0;left:0}
.newsletter{position:absolute;top:80px;width:100%;text-align:center}
.newsletter h2{font:400 28px var(--head);color:var(--navy);text-transform:uppercase}
.news-form{display:inline-flex;margin-top:20px;gap:10px}
.news-form .field{width:330px;height:40px;border:1px solid var(--line);background:#fff;border-radius:20px;padding:0 18px;font-size:12px;color:var(--muted);display:flex;align-items:center}
.news-form .btn{padding:12px 26px}
.footer-brand{position:absolute;top:228px;width:100%;display:flex;justify-content:center}
.footer-brand .brand{font-size:54px}
.footer-brand .brand .dot{width:22px;height:22px}
.socials{position:absolute;top:320px;left:540px;display:flex;gap:12px}
.socials span{width:30px;height:30px;border-radius:50%;background:var(--navy)}
.pill{position:absolute;top:296px;display:inline-flex;align-items:center;gap:8px;background:var(--navy);color:#fff;border-radius:20px;padding:10px 18px;font:500 12px var(--body)}
.footer-col{position:absolute;top:370px;font-size:11px;line-height:1.6;color:var(--muted)}
.footer-col h4{font:700 12px var(--body);color:var(--navy);text-transform:uppercase;margin-bottom:4px}
.footer-note{position:absolute;top:380px;left:430px;width:340px;text-align:center;font-size:11px;line-height:1.6;color:var(--muted)}
.bottom-bar{height:64px;background:var(--foot-bar);display:flex;align-items:center;justify-content:center;font-size:11px;color:#fff;letter-spacing:.5px}
</style>
</head>
<body>

<header class="site-header">
  <div class="brand"><span class="dot"></span>Norvalith</div>
  <nav class="main-nav">
    <span class="active">Home</span><span>About Us</span><span>Services</span><span>Insights</span><span>Join Us</span><span>Contact Us</span>
  </nav>
</header>

<section class="hero">
  <div class="hero-photo" role="img" aria-label="City skyline at dusk with glowing network connection lines in purple and pink tones"></div>
  <h1 class="hero-title">Transformation<br>Delivered</h1>
  <svg class="hero-wave" width="1200" height="90" viewBox="0 0 1200 90" aria-hidden="true">
    <path d="M0 60 C150 20 300 80 450 50 C600 20 750 80 900 45 C1020 20 1120 40 1200 30 L1200 90 L0 90 Z" fill="#ffffff"/>
  </svg>
</section>

<section class="intro">
  <svg class="intro-media" viewBox="0 0 430 420" role="img" aria-label="Consultant working at a laptop in a modern office, framed in a rounded blob shape">
    <defs>
      <linearGradient id="introPhoto" x1="0" y1="0" x2="1" y2="1">
        <stop offset="0" stop-color="#6d8fb8"/><stop offset=".6" stop-color="#2d4566"/><stop offset="1" stop-color="#1b2a40"/>
      </linearGradient>
    </defs>
    <path d="M40 300 C10 230 30 120 110 70 C200 10 330 20 390 90 C440 160 420 280 340 340 C260 400 90 400 40 300 Z" fill="#f3c316"/>
    <path d="M60 280 C40 200 70 110 150 70 C240 30 350 60 380 140 C410 230 360 320 270 350 C180 380 80 360 60 280 Z" fill="url(#introPhoto)"/>
    <path d="M30 330 C120 410 300 410 380 330" stroke="#1d3f7a" stroke-width="3" fill="none"/>
  </svg>
  <div class="badge">Our 1,000+ experienced ecosystem</div>
  <div class="intro-copy">
    <h2 class="section-title">Transformation Delivered.</h2>
    <p>We do more for our customers than implement software. We listen. We work to understand where they are in their transformation journey and where they want to go. We partner with them to close the gap between the vision and the software they end up with.</p>
    <ul class="ticks">
      <li>Focus on business value, with an emphasis on delivering value quickly</li>
      <li>Meet our customers where they are without leading them back to the beginning of their journey</li>
      <li>Provide a wide range of services from strategy to product support</li>
      <li>Commit to our customer's long-term success</li>
    </ul>
    <p>Norvalith is business transformation, delivered.</p>
    <span class="btn"><span class="ico"></span>Contact Us</span>
  </div>
</section>

<section class="services">
  <h2 class="section-title">Transformation Supported<br>by Technology</h2>
  <p class="sub">Find out how Norvalith can help you put all the pieces together and get them done.</p>
  <div class="service-row">
    <div class="service-card">
      <div class="service-icon"><svg width="40" height="40" viewBox="0 0 40 40" aria-hidden="true"><circle cx="20" cy="20" r="12" fill="none" stroke="#1d3f7a" stroke-width="3"/><path d="M20 8v24M8 20h24" stroke="#2f6fc4" stroke-width="3"/></svg></div>
      <h3>Business Transformation</h3><p>Define and execute your strategy</p>
    </div>
    <div class="service-card">
      <div class="service-icon"><svg width="40" height="40" viewBox="0 0 40 40" aria-hidden="true"><rect x="6" y="8" width="28" height="20" rx="2" fill="none" stroke="#1d3f7a" stroke-width="3"/><path d="M12 34h16" stroke="#1d3f7a" stroke-width="3"/></svg></div>
      <h3>ERP Implementations</h3><p>Deploy, upgrade and support ERP to match your needs</p>
    </div>
    <div class="service-card">
      <div class="service-icon"><svg width="40" height="40" viewBox="0 0 40 40" aria-hidden="true"><rect x="6" y="8" width="28" height="24" rx="3" fill="none" stroke="#f3c316" stroke-width="3"/><path d="M12 16h16M12 22h10" stroke="#1d3f7a" stroke-width="3"/></svg></div>
      <h3>CRM Implementations</h3><p>Put your customers at the centre of the business</p>
    </div>
    <div class="service-card">
      <div class="service-icon"><svg width="40" height="40" viewBox="0 0 40 40" aria-hidden="true"><path d="M8 32V20M16 32V12M24 32V16M32 32V8" stroke="#1d3f7a" stroke-width="4"/></svg></div>
      <h3>BI and Data</h3><p>Transform data into better decisions</p>
    </div>
  </div>
</section>

<section class="people">
  <div class="people-copy">
    <h2 class="section-title">It's the People</h2>
    <p>The world has changed in the past twenty years. The people you need might not all work for one company. Our clients need the best resources available quickly. That is why, in addition to our team of experts, we partner with:</p>
    <ul class="ticks">
      <li>A large network of expert consultants who we know from our past projects</li>
      <li>Service providers all over the world to provide the resources and tools that are right for you</li>
    </ul>
    <p>People are invaluable at the centre of our customer's success. Find out how we can add our experts to yours.</p>
    <span class="btn"><span class="ico"></span>Get in Touch</span>
  </div>
  <svg class="people-media" viewBox="0 0 420 420" role="img" aria-label="Smiling businesswoman with glasses working at a desk, framed in a rounded blob shape">
    <defs>
      <linearGradient id="peoplePhoto" x1="0" y1="0" x2="1" y2="1">
        <stop offset="0" stop-color="#e8ecf1"/><stop offset=".55" stop-color="#b9c3cf"/><stop offset="1" stop-color="#4a4f5a"/>
      </linearGradient>
    </defs>
    <path d="M30 220 C20 120 110 40 220 40 C330 40 400 120 395 220 C390 330 300 390 200 385 C100 380 40 320 30 220 Z" fill="url(#peoplePhoto)"/>
    <path d="M20 120 C60 30 200 10 290 40" stroke="#1d3f7a" stroke-width="3" fill="none"/>
    <path d="M130 400 C240 420 360 370 405 260" stroke="#f3c316" stroke-width="4" fill="none"/>
  </svg>
</section>

<section class="testimonials">
  <div class="quote-card side left">Our project was delivered on time with a team that understood our business from the very first meeting. We now have a platform that grows with us every year.</div>
  <div class="quote-card center">
    <div class="avatar" role="img" aria-label="Portrait of the client quoted"></div>
    <p>Norvalith listened before they proposed anything. They understood where we were and where we wanted to go, and brought the right people and software to close that gap. Our transformation finally matched our vision, and the results came quickly.</p>
    <p class="quote-name">DANA R.</p>
  </div>
  <div class="quote-card side right">The team brought partners we would never have found alone. Their experts fitted right in with ours and stayed with us long after launch.</div>
  <span class="arrow" style="left:228px"><svg width="12" height="12" viewBox="0 0 12 12" aria-hidden="true"><path d="M8 1L3 6l5 5" stroke="#fff" stroke-width="2" fill="none"/></svg></span>
  <span class="arrow" style="left:938px"><svg width="12" height="12" viewBox="0 0 12 12" aria-hidden="true"><path d="M4 1l5 5-5 5" stroke="#fff" stroke-width="2" fill="none"/></svg></span>
</section>

<section class="technologies">
  <h2 class="section-title">Technologies</h2>
  <div class="tech-row">
    <div class="tech-tile">
      <div class="fill" role="img" aria-label="Hand touching a glowing ERP interface on a teal background" style="background:linear-gradient(160deg,#3fb2c6,#1c6a8c 60%,#123c5a)"></div>
      <div class="label">ERP<br>Technologies</div>
    </div>
    <div class="tech-tile">
      <div class="fill" role="img" aria-label="Hands holding a tablet with data charts in pink and blue light" style="background:linear-gradient(160deg,#c8d7f0,#d99ad0 55%,#6c5aa8)"></div>
      <div class="label">Data<br>Technologies</div>
    </div>
    <div class="tech-tile">
      <div class="fill" role="img" aria-label="Businessman touching a network of customer icons on a purple background" style="background:linear-gradient(160deg,#8e79c8,#5a3f96 55%,#2c1f5c)"></div>
      <div class="label">CRM<br>Technologies</div>
    </div>
  </div>
</section>

<section class="partners">
  <span class="arrow" style="left:125px;top:58px;background:none"><svg width="14" height="14" viewBox="0 0 12 12" aria-hidden="true"><path d="M8 1L3 6l5 5" stroke="#2c3440" stroke-width="2" fill="none"/></svg></span>
  <div class="partner-row">
    <div class="partner"><span class="mark" style="width:110px;background:#3fa34d"></span></div>
    <div class="partner"><span class="mark" style="width:120px;background:#29b5e8"></span></div>
    <div class="partner"><span class="mark" style="width:120px;background:#d0312d"></span></div>
    <div class="partner"><span class="mark" style="width:110px;background:#f3a21b"></span></div>
  </div>
  <span class="arrow" style="left:1045px;top:58px;background:none"><svg width="14" height="14" viewBox="0 0 12 12" aria-hidden="true"><path d="M4 1l5 5-5 5" stroke="#2c3440" stroke-width="2" fill="none"/></svg></span>
</section>

<footer class="site-footer">
  <svg class="footer-wave" width="1200" height="60" viewBox="0 0 1200 60" aria-hidden="true">
    <path d="M0 0 L1200 0 L1200 20 C1000 50 850 10 650 30 C450 50 250 15 0 35 Z" fill="#ffffff"/>
  </svg>
  <div class="newsletter">
    <h2>Signup for Newsletter</h2>
    <div class="news-form"><span class="field">Enter your email</span><span class="btn">Subscribe Now</span></div>
  </div>
  <div class="footer-brand"><div class="brand"><span class="dot"></span>Norvalith</div></div>
  <span class="pill" style="left:160px"><svg width="14" height="14" viewBox="0 0 14 14" aria-hidden="true"><path d="M3 1l3 3-2 2c1 2 2 3 4 4l2-2 3 3-2 2C6 13 1 8 1 3z" fill="#fff"/></svg>(555) 384-1902</span>
  <span class="pill" style="left:830px"><svg width="14" height="14" viewBox="0 0 14 14" aria-hidden="true"><circle cx="7" cy="7" r="6" stroke="#fff" stroke-width="1.5" fill="none"/><path d="M1 7h12M7 1c3 3 3 9 0 12M7 1c-3 3-3 9 0 12" stroke="#fff" stroke-width="1.2" fill="none"/></svg>norvalithconsulting.com</span>
  <div class="socials"><span></span><span></span><span></span><span></span></div>
  <div class="footer-col" style="left:160px"><h4>Address</h4>210 Harbor Point Ave, Suite 14<br>Riverton, MN 55401</div>
  <p class="footer-note">Norvalith helps businesses close the gap between their transformation vision and the software they use, with the right people and partners.</p>
  <div class="footer-col" style="left:830px"><h4>Office Hours</h4>Monday – Saturday: 9AM – 6PM<br>24-Hour Emergency Service Available</div>
</footer>

<div class="bottom-bar">Copyright © 2024 Norvalith. All rights reserved.</div>

</body>
</html>
```